Book Cover Design for a Novella

This book is a whimsical book about random philosophical thoughts. The size of the book is 4X6 inches, about 140 pages long. I would like the background color to be maroon. The title of the book is The Lantern Keeper's Crooked Almanac of Days, and the author name is Delia Marwood. I would like the lettering to either be black or gold, in a font that looks like handwriting. From the lower left corner of the front cover, I would like there to be a gold-colored gardenia.
On the back cover, this is the book summary/description: “We are meant to share our hearts, not give them away. Vulnerability is not the act of placing your heart in someone else’s hands, saying, ‘Keep this safe for me.’ Vulnerability is wearing your heart on your sleeve, showing others your beauty, truths, and fears, and trusting that they will respect you.”
For the author's bio: Delia Marwood is a native of Boulder, Colorado. She enjoys spending time with her cats, eating pasta, and contemplating random things, such as banana spiders, sewage systems, and other huge things that scare her.
I would like all the writing on the back to be in a black, regular font.
I will upload the author's photo, which I would like to be put next to the bio, and I will also attach a rough sketch of what I'd like the cover to look like. Message me with any questions! Thanks.

```html
<!DOCTYPE html>
<html lang="en">
<head>
<meta charset="utf-8">
<title>The Lantern Keeper's Crooked Almanac of Days — Delia Marwood</title>
<link rel="stylesheet" href="https://fonts.googleapis.com/css2?family=Great+Vibes&display=swap">
<style>
  :root {
    --maroon-core: #7d0202;
    --maroon-mid: #5e0000;
    --maroon-edge: #360000;
    --gold: #e2ad4c;
    --gold-light: #f4d27f;
    --gold-shadow: rgba(25, 0, 0, 0.75);
    --bloom-bright: #ffb43a;
    --bloom-deep: #f08a12;
    --leaf: #2f4a22;
  }
  html, body {
    margin: 0;
    padding: 0;
    width: 798px;
    height: 1200px;
    overflow: hidden;
    background: var(--maroon-edge);
  }
  .cover {
    position: relative;
    width: 798px;
    height: 1200px;
    overflow: hidden;
    background:
      radial-gradient(ellipse 75% 60% at 50% 45%, var(--maroon-core) 0%, var(--maroon-mid) 55%, var(--maroon-edge) 100%);
  }
  .cover-title {
    position: absolute;
    top: 118px;
    left: 0;
    width: 100%;
    margin: 0;
    text-align: center;
    font-family: "Great Vibes", cursive;
    font-weight: 400;
    color: var(--gold);
    background: linear-gradient(180deg, var(--gold-light) 0%, var(--gold) 55%, #b9822c 100%);
    -webkit-background-clip: text;
    background-clip: text;
    -webkit-text-fill-color: transparent;
    filter: drop-shadow(3px 4px 3px var(--gold-shadow));
  }
  .cover-title .title-line {
    display: block;
    line-height: 1;
  }
  .title-line--major { font-size: 74px; margin-bottom: 18px; }
  .title-line--minor { font-size: 56px; margin-bottom: 18px; }
  .gardenia {
    position: absolute;
    left: 60px;
    top: 672px;
    width: 560px;
    height: 528px;
    border-radius: 48% 52% 0 0 / 46% 46% 0 0;
    background:
      radial-gradient(ellipse 45% 42% at 48% 40%, var(--bloom-bright) 0%, var(--bloom-deep) 55%, rgba(240,138,18,0) 80%),
      radial-gradient(ellipse 60% 70% at 55% 60%, var(--leaf) 0%, rgba(47,74,34,0.6) 55%, rgba(47,74,34,0) 80%);
  }
  .cover-author {
    position: absolute;
    right: 24px;
    bottom: 22px;
    margin: 0;
    font-family: "Great Vibes", cursive;
    font-weight: 400;
    font-size: 68px;
    line-height: 1;
    color: var(--gold);
    text-shadow: 2px 3px 3px var(--gold-shadow);
  }
</style>
</head>
<body>
  <main class="cover">
    <h1 class="cover-title">
      <span class="title-line title-line--major">The Lantern Keeper's</span>
      <span class="title-line title-line--major">Crooked Almanac</span>
      <span class="title-line title-line--minor">of Days</span>
    </h1>
    <div class="gardenia" role="img" aria-label="Photograph of an orange-gold gardenia bloom with dark green leaves rising from the lower left"></div>
    <p class="cover-author">Delia Marwood</p>
  </main>
</body>
</html>
```